Letterhead for Midwest Law Firm

Our law firm does estate planning and trust administration in Wisconsin and Illinois. We recently obtained a new logo and need to incorporate it into new stationary. The stationary needs to list out the attorneys at the firm, but we will want 3 variations, one with three attorneys, one with six, and one with six plus the names of states where each is licensed to practice (possibly as an asterisk with notation somewhere towards bottom of page. As with most traditional law practices, letterhead should be conservative and convey predictability and reliability. We view our brand as being primarily reliability, with prestige as a secondary element. We are upmarket, but would like to avoid seeming pretentious or "slick". We are a smaller firm with a personal touch.

Target Market(s)

Affluent Midwestern Americans approaching at or approaching retirement age.

Industry/Entity Type

Legal

Font styles to use
Serif
Sans Serif

Requirements
Must have
• Must use our logo. Must comply with Northgate Counsel Guild Ethics rules: https://www.quarvenlex.org/rules/offices/docs/plmtk41annotated.pdf. Must be conventional. Must list names of attorneys and provide contact information for firm. Note that we are asking for three designs with very minor variations. Also, designer must provide letterhead in a format that is industry-standard for stationary printers.
Nice to have
• We would appreciate an alternate version that will look reasonable when printed on a black-and-white printer. Designer can use judgment as to whether to have use grayscale, black/white, or something in between.
Should not have
• No "motto" or "visit our website" extraneous materials. putting the website address somewhere is fine, but overall there is a lot of required text, and we'd like to not appear cluttered.

```html
<!DOCTYPE html>
<html lang="en">
<head>
<meta charset="utf-8">
<title>Halvorsen &amp; Pike LLP — Letterhead Set</title>
<link href="https://fonts.googleapis.com/css2?family=Libre+Baskerville:wght@400;700&family=Open+Sans:wght@400&display=swap" rel="stylesheet">
<style>
:root{
  --backdrop:#e4e4e5;
  --paper:#fafafb;
  --navy:#2b2940;
  --gold:#f0a623;
  --blue:#2a9fd8;
  --body:#555559;
  --ink:#3a3a44;
}
*{margin:0;padding:0;box-sizing:border-box}
html,body{width:947px;height:1200px;overflow:hidden;background:var(--backdrop)}
.canvas{position:relative;width:947px;height:1200px}
.sheet{position:absolute;width:325px;height:453px;background:var(--paper);box-shadow:0 4px 10px rgba(0,0,0,.08)}
.sheet--a{left:130px;top:88px}
.sheet--b{left:484px;top:86px;width:322px}
.sheet--c{left:130px;top:655px}
.sheet--cover{left:484px;top:655px;width:322px;background:var(--navy)}

.brand{position:absolute;left:0;right:0;top:22px;text-align:center;font-family:'Libre Baskerville',serif;font-weight:700;color:var(--navy)}
.brand__dot{display:block;width:16px;height:16px;border-radius:50%;background:var(--gold);margin:0 auto 10px}
.brand__name{display:block;font-size:8.6px;line-height:1}
.brand__llp{display:block;font-size:5px;margin-top:2px}

.roster{position:absolute;top:71px;font-family:'Libre Baskerville',serif;font-size:4.3px;line-height:8px;color:var(--ink);text-transform:uppercase;letter-spacing:.1px}
.roster--left{left:29px}
.roster--right{left:182px}
.roster small{text-transform:none;font-size:4px}

.letter{position:absolute;left:29px;right:30px;font-family:'Open Sans',sans-serif;font-size:5.75px;line-height:8.8px;color:var(--body)}
.letter p{text-align:justify;margin-bottom:8.8px}
.letter .salutation,.letter .closing{text-align:left;margin-bottom:8.5px}
.signature{display:block;width:40px;height:36px;background:linear-gradient(135deg,#e9e9ec,#d8d8dc);border-radius:2px;margin-top:4px}

.contact{position:absolute;left:29px;top:421px;font-family:'Libre Baskerville',serif;font-size:5.4px;line-height:9px;color:var(--ink)}
.contact svg{width:5px;height:5px;vertical-align:-0.5px;fill:var(--blue)}

.cover-brand{position:absolute;left:0;right:0;top:200px;text-align:center;font-family:'Libre Baskerville',serif;font-weight:700;color:#fff}
.cover-brand .brand__dot{width:30px;height:30px;margin-bottom:16px}
.cover-brand .brand__name{font-size:18.5px}
.cover-brand .brand__llp{font-size:10px;margin-top:5px}
</style>
</head>
<body>
<div class="canvas">

  <!-- Six attorneys -->
  <section class="sheet sheet--a">
    <div class="brand"><span class="brand__dot"></span><span class="brand__name">Halvorsen &amp; Pike</span><span class="brand__llp">LLP</span></div>
    <div class="roster roster--left">Daniel C. Halvorsen<br>Thomas J. Pike<br>Peter R. Halvorsen</div>
    <div class="roster roster--right">Lucas A. Brennick, Sr. Associate<br>Claire J. Donnelly, Sr. Associate<br>Erin A. Koval, Sr. Associate<br>Megan A. Thorsby, Associate</div>
    <div class="letter" style="top:127px">
      <p class="salutation">Dear customer,</p>
      <p>Lorem ipsum dolor sit amet, consectetur adipisicing elit, sed do eiusmod tempor incididunt ut labore et dolore magna aliqua. Ut enim ad minim veniam, quis nostrud exercitation ullamco laboris nisi ut aliquip ex ea commodo consequat. Duis aute irure dolor in reprehenderit in voluptate velit esse cillum dolore eu fugiat nulla pariatur. Excepteur sint occaecat cupidatat non proident, sunt in culpa qui officia deserunt mollit anim id est laborum.</p>
      <p>Lorem ipsum dolor sit amet, consectetur adipisicing elit, sed do eiusmod tempor incididunt ut labore et dolore magna aliqua. Ut enim ad minim veniam, quis nostrud exercitation ullamco laboris nisi ut aliquip ex ea commodo consequat. Duis aute irure dolor in reprehenderit in voluptate velit esse cillum dolore eu fugiat nulla pariatur. Excepteur sint occaecat cupidatat non proident, sunt in culpa qui officia deserunt mollit anim id est laborum.</p>
      <p>Lorem ipsum dolor sit amet, consectetur adipisicing elit, sed do eiusmod tempor incididunt ut labore et dolore magna aliqua. Ut enim ad minim veniam, quis nostrud exercitation ullamco laboris nisi ut aliquip ex ea commodo consequat. Duis aute irure dolor in reprehenderit in voluptate velit esse cillum dolore eu fugiat nulla pariatur. Excepteur sint occaecat cupidatat non proident, sunt in culpa qui officia deserunt mollit anim id est laborum.</p>
      <p>Lorem ipsum dolor sit amet, consectetur adipisicing elit, sed do eiusmod tempor incididunt ut labore et dolore magna aliqua. Ut enim ad minim veniam, quis nostrud exercitation ullamco laboris nisi ut aliquip ex ea commodo consequat. Duis aute irure dolor in reprehenderit.</p>
      <p class="closing">Yours Sincerely,</p>
      <span class="signature" role="img" aria-label="Handwritten signature"></span>
    </div>
    <div class="contact">
      <svg viewBox="0 0 10 10"><path d="M2 1l2 2-1 1.5c.8 1.5 1.5 2.2 3 3L7.5 6l2 2-1.5 1.5C4.5 9 1 5.5.5 2z"/></svg> 414-555-0142
      <svg viewBox="0 0 10 10"><rect x="2" y="1" width="6" height="3"/><rect x="0" y="4" width="10" height="4" rx="1"/><rect x="2" y="7" width="6" height="3"/></svg> 414-555-0187<br>
      218 E. Harbor Street, Suite 400&nbsp; Milwaukee, WI&nbsp; 53202
    </div>
  </section>

  <!-- Six attorneys, alternate -->
  <section class="sheet sheet--b">
    <div class="brand"><span class="brand__dot"></span><span class="brand__name">Halvorsen &amp; Pike</span><span class="brand__llp">LLP</span></div>
    <div class="roster roster--left">Daniel C. Halvorsen<br>Thomas J. Pike<br>Peter R. Halvorsen</div>
    <div class="roster roster--right" style="left:181px">Lucas A. Brennick, Sr. Associate<br>Claire J. Donnelly, Sr. Associate<br>Erin A. Koval, Sr. Associate</div>
    <div class="letter" style="top:123px">
      <p class="salutation">Dear customer,</p>
      <p>Lorem ipsum dolor sit amet, consectetur adipisicing elit, sed do eiusmod tempor incididunt ut labore et dolore magna aliqua. Ut enim ad minim veniam, quis nostrud exercitation ullamco laboris nisi ut aliquip ex ea commodo consequat. Duis aute irure dolor in reprehenderit in voluptate velit esse cillum dolore eu fugiat nulla pariatur. Excepteur sint occaecat cupidatat non proident, sunt in culpa qui officia deserunt mollit anim id est laborum.</p>
      <p>Lorem ipsum dolor sit amet, consectetur adipisicing elit, sed do eiusmod tempor incididunt ut labore et dolore magna aliqua. Ut enim ad minim veniam, quis nostrud exercitation ullamco laboris nisi ut aliquip ex ea commodo consequat. Duis aute irure dolor in reprehenderit in voluptate velit esse cillum dolore eu fugiat nulla pariatur. Excepteur sint occaecat cupidatat non proident, sunt in culpa qui officia deserunt mollit anim id est laborum.</p>
      <p>Lorem ipsum dolor sit amet, consectetur adipisicing elit, sed do eiusmod tempor incididunt ut labore et dolore magna aliqua. Ut enim ad minim veniam, quis nostrud exercitation ullamco laboris nisi ut aliquip ex ea commodo consequat. Duis aute irure dolor in reprehenderit in voluptate velit esse cillum dolore eu fugiat nulla pariatur. Excepteur sint occaecat cupidatat non proident, sunt in culpa qui officia deserunt mollit anim id est laborum.</p>
      <p>Lorem ipsum dolor sit amet, consectetur adipisicing elit, sed do eiusmod tempor incididunt ut labore et dolore magna aliqua. Ut enim ad minim veniam, quis nostrud exercitation ullamco laboris nisi ut aliquip ex ea commodo consequat. Duis aute irure dolor in reprehenderit.</p>
      <p class="closing">Yours Sincerely,</p>
      <span class="signature" role="img" aria-label="Handwritten signature"></span>
    </div>
    <div class="contact">
      <svg viewBox="0 0 10 10"><path d="M2 1l2 2-1 1.5c.8 1.5 1.5 2.2 3 3L7.5 6l2 2-1.5 1.5C4.5 9 1 5.5.5 2z"/></svg> 414-555-0142
      <svg viewBox="0 0 10 10"><rect x="2" y="1" width="6" height="3"/><rect x="0" y="4" width="10" height="4" rx="1"/><rect x="2" y="7" width="6" height="3"/></svg> 414-555-0187<br>
      218 E. Harbor Street, Suite 400&nbsp; Milwaukee, WI&nbsp; 53202
    </div>
  </section>

  <!-- Three attorneys -->
  <section class="sheet sheet--c">
    <div class="brand"><span class="brand__dot"></span><span class="brand__name">Halvorsen &amp; Pike</span><span class="brand__llp">LLP</span></div>
    <div class="roster roster--left" style="line-height:7.5px">Daniel C. Halvorsen, <small>Attorney</small><br>Laura M. Stenberg, <small>Paralegal</small></div>
    <div class="roster roster--right" style="left:198px">Peter R. Halvorsen, <small>Attorney</small></div>
    <div class="letter" style="top:120px">
      <p class="salutation">Dear customer,</p>
      <p>Lorem ipsum dolor sit amet, consectetur adipisicing elit, sed do eiusmod tempor incididunt ut labore et dolore magna aliqua. Ut enim ad minim veniam, quis nostrud exercitation ullamco laboris nisi ut aliquip ex ea commodo consequat. Duis aute irure dolor in reprehenderit in voluptate velit esse cillum dolore eu fugiat nulla pariatur. Excepteur sint occaecat cupidatat non proident, sunt in culpa qui officia deserunt mollit anim id est laborum.</p>
      <p>Lorem ipsum dolor sit amet, consectetur adipisicing elit, sed do eiusmod tempor incididunt ut labore et dolore magna aliqua. Ut enim ad minim veniam, quis nostrud exercitation ullamco laboris nisi ut aliquip ex ea commodo consequat. Duis aute irure dolor in reprehenderit in voluptate velit esse cillum dolore eu fugiat nulla pariatur. Excepteur sint occaecat cupidatat non proident, sunt in culpa qui officia deserunt mollit anim id est laborum.</p>
      <p>Lorem ipsum dolor sit amet, consectetur adipisicing elit, sed do eiusmod tempor incididunt ut labore et dolore magna aliqua. Ut enim ad minim veniam, quis nostrud exercitation ullamco laboris nisi ut aliquip ex ea commodo consequat. Duis aute irure dolor in reprehenderit in voluptate velit esse cillum dolore eu fugiat nulla pariatur. Excepteur sint occaecat cupidatat non proident, sunt in culpa qui officia deserunt mollit anim id est laborum.</p>
      <p>Lorem ipsum dolor sit amet, consectetur adipisicing elit, sed do eiusmod tempor incididunt ut labore et dolore magna aliqua. Ut enim ad minim veniam, quis nostrud exercitation ullamco laboris nisi ut aliquip ex ea commodo consequat. Duis aute irure dolor in reprehenderit.</p>
      <p class="closing">Yours Sincerely,</p>
      <span class="signature" role="img" aria-label="Handwritten signature"></span>
    </div>
    <div class="contact">
      <svg viewBox="0 0 10 10"><path d="M2 1l2 2-1 1.5c.8 1.5 1.5 2.2 3 3L7.5 6l2 2-1.5 1.5C4.5 9 1 5.5.5 2z"/></svg> 414-555-0142
      <svg viewBox="0 0 10 10"><rect x="2" y="1" width="6" height="3"/><rect x="0" y="4" width="10" height="4" rx="1"/><rect x="2" y="7" width="6" height="3"/></svg> 414-555-0187<br>
      218 E. Harbor Street, Suite 400&nbsp; Milwaukee, WI&nbsp; 53202
    </div>
  </section>

  <!-- Reverse side -->
  <section class="sheet sheet--cover">
    <div class="cover-brand"><span class="brand__dot"></span><span class="brand__name">Halvorsen &amp; Pike</span><span class="brand__llp">LLP</span></div>
  </section>

</div>
</body>
</html>
```